Construction company- stationary project
business card, letterhead, envelopes, presentation folder
Construction company- stationary project -
Creative Brief
Professional
Brent Halloway
38 Percival Ln. Millbrook, NY 12545
brent.halloway@ridgefold-builders.com
www.ridgefold-builders.com
Residential contractor focused on design build, custom, and restoration projects. Emphasizing team concept
open to ideas possibly the logo

```html
<!DOCTYPE html>
<html lang="en">
<head>
<meta charset="utf-8">
<title>Ridgefold Builders — Stationery Set</title>
<link href="https://fonts.googleapis.com/css2?family=Cinzel:wght@400;600&display=swap" rel="stylesheet">
<style>
  :root {
    --espresso: #4e1a10;
    --umber: #6b2a18;
    --copper: #c9824f;
    --paper: #ffffff;
    --edge: #c9c9c9;
    --ink: #5a2416;
    --stage: #ffffff;
  }
  * { box-sizing: border-box; margin: 0; padding: 0; }
  html, body { width: 1200px; height: 818px; overflow: hidden; background: var(--stage); }
  body { position: relative; font-family: "Cinzel", "Times New Roman", serif; color: var(--ink); }

  .sheet {
    position: absolute; background: var(--paper);
    border: 1px solid var(--edge);
    box-shadow: 1px 2px 4px rgba(0,0,0,0.18);
  }
  .band {
    position: absolute; left: 0; right: 0;
    background:
      radial-gradient(ellipse 30% 120% at 62% 50%, var(--copper) 0%, rgba(201,130,79,0) 100%),
      linear-gradient(90deg, var(--espresso), var(--umber) 50%, var(--espresso));
  }
  .company { position: absolute; text-align: center; font-weight: 600; color: var(--ink); line-height: 1.1; }
  .company .line { display: block; }
  .small { font-size: 10px; letter-spacing: 0.4px; color: var(--ink); line-height: 1.4; }

  /* Letterhead */
  .letterhead { left: 29px; top: 58px; width: 583px; height: 730px; z-index: 1; }
  .letterhead .band { top: 14px; height: 48px; }
  .letterhead .company { left: 18px; top: 96px; width: 160px; font-size: 16px; }
  .letterhead .footer { position: absolute; left: 22px; bottom: 24px; }

  /* Business card front */
  .card-front { left: 631px; top: 53px; width: 194px; height: 116px; z-index: 1; }
  .card-front .band { top: 0; height: 28px; }
  .card-front .company { left: 4px; top: 33px; width: 84px; font-size: 8px; }
  .card-front .holder { position: absolute; left: 100px; top: 38px; font-size: 10px; }
  .card-front .contact { position: absolute; left: 8px; top: 58px; font-size: 6px; line-height: 1.45; }

  /* Business card back */
  .card-back {
    left: 878px; top: 286px; width: 245px; height: 132px; z-index: 4;
    background:
      radial-gradient(ellipse 55% 75% at 50% 50%, var(--copper) 0%, rgba(201,130,79,0) 100%),
      linear-gradient(90deg, var(--espresso), var(--umber) 50%, var(--espresso));
    display: flex; align-items: center; justify-content: center;
  }
  .card-back .name-mark { color: var(--paper); font-weight: 600; font-size: 17px; letter-spacing: 1px; }

  /* Envelope */
  .envelope-flap { position: absolute; left: 526px; top: 372px; width: 646px; height: 118px; z-index: 2; }
  .envelope-flap svg { display: block; }
  .envelope-flap .name-mark {
    position: absolute; left: 0; right: 0; top: 62px; text-align: center;
    color: var(--paper); font-weight: 600; font-size: 20px; letter-spacing: 1px;
  }
  .envelope { left: 526px; top: 487px; width: 646px; height: 300px; z-index: 3; }
  .envelope .band { top: 24px; height: 43px; }
  .envelope .company { left: 6px; top: 76px; width: 150px; font-size: 15px; }
  .envelope .return { position: absolute; left: 12px; top: 132px; font-size: 11px; }
</style>
</head>
<body>

  <section class="sheet letterhead" aria-label="Letterhead">
    <div class="band"></div>
    <div class="company"><span class="line">Ridgefold</span><span class="line">Builders</span></div>
    <p class="small footer">38 Percival Ln. Ashcombe, VT 05341<br>Cell: 845-555-0172 | www.ridgefold-builders.com</p>
  </section>

  <section class="sheet card-front" aria-label="Business card front">
    <div class="band"></div>
    <div class="company"><span class="line">Ridgefold</span><span class="line">Builders</span></div>
    <p class="holder">Brent Halloway</p>
    <p class="contact">38 Percival Ln.<br>Ashcombe, VT 05341<br>Cell: 845-555-0172<br>Email: brent.halloway@ridgefold-builders.com<br>www.ridgefold-builders.com</p>
  </section>

  <section class="sheet card-back" aria-label="Business card back">
    <span class="name-mark">Ridgefold</span>
  </section>

  <section class="envelope-flap" aria-label="Envelope back flap">
    <svg width="646" height="118" viewBox="0 0 646 118">
      <defs>
        <radialGradient id="flapGlow" cx="0.5" cy="0.55" r="0.45">
          <stop offset="0" stop-color="#c9824f"/>
          <stop offset="1" stop-color="#6b2a18" stop-opacity="0"/>
        </radialGradient>
        <linearGradient id="flapBase" x1="0" x2="1">
          <stop offset="0" stop-color="#4e1a10"/>
          <stop offset="0.5" stop-color="#6b2a18"/>
          <stop offset="1" stop-color="#4e1a10"/>
        </linearGradient>
      </defs>
      <path d="M0 16 Q0 0 16 0 L630 0 Q646 0 646 16 L646 114 Q323 100 0 114 Z" fill="url(#flapBase)"/>
      <path d="M0 16 Q0 0 16 0 L630 0 Q646 0 646 16 L646 114 Q323 100 0 114 Z" fill="url(#flapGlow)"/>
    </svg>
    <span class="name-mark">Ridgefold</span>
  </section>

  <section class="sheet envelope" aria-label="Envelope front">
    <div class="band"></div>
    <div class="company"><span class="line">Ridgefold</span><span class="line">Builders</span></div>
    <p class="small return">38 Percival Ln.<br>Ashcombe, VT 05341</p>
  </section>

</body>
</html>
```